Business Card design for Recruiter providing Recruitment Staff Augmentation services

I need a double sided business card. I have used Zek to print cards in the past and really like their quality. I have a logo but need to change the tagline that is part of the graphic.

The tagline currently reads and Connnecting people with careers - but it should be removed.

The back should look like a notecard for writing a to do list with the first to-do Augment Recruiting Staff

```html
<!DOCTYPE html>
<html lang="en">
<head>
<meta charset="utf-8">
<title>Talent Summit – Business Card</title>
<link rel="stylesheet" href="https://fonts.googleapis.com/css2?family=Questrial&display=swap">
<style>
  :root {
    --page: #ece7df;
    --navy: #134a6b;
    --navy-line: #1d4d6c;
    --orange: #d4532c;
    --paper: #ffffff;
    --paper-back: #f1f2f3;
    --ink-light: #e6eef3;
    --font: "Questrial", "Century Gothic", sans-serif;
  }
  html, body {
    margin: 0;
    width: 1200px;
    height: 1023px;
    overflow: hidden;
    background: var(--page);
    font-family: var(--font);
  }
  .canvas { position: relative; width: 1200px; height: 1023px; }
  .card {
    position: absolute;
    width: 540px;
    height: 308px;
    overflow: hidden;
    box-shadow: 0 6px 18px rgba(60, 45, 25, 0.25);
  }
  .card-front { left: 70px; top: 150px; background: var(--paper); }
  .card-back  { left: 590px; top: 565px; background: var(--paper-back); }
  .card-art { position: absolute; inset: 0; }

  .front-top {
    position: absolute;
    left: 0; top: 0;
    width: 100%;
    height: 192px;
    background: var(--navy);
  }
  .front-rule {
    position: absolute;
    left: 0; top: 192px;
    width: 100%;
    height: 6px;
    background: var(--orange);
  }

  .contact {
    position: absolute;
    right: 30px;
    top: 24px;
    text-align: right;
    color: var(--ink-light);
  }
  .contact-name { font-size: 19px; letter-spacing: 0.3px; }
  .contact-title { font-size: 13px; margin-top: 3px; }
  .contact-lines { margin-top: 14px; display: grid; grid-template-columns: auto 16px; column-gap: 10px; row-gap: 4px; align-items: center; font-size: 12.5px; }
  .contact-lines svg { width: 13px; height: 13px; }
  .contact-address { margin-top: 12px; font-size: 12.5px; line-height: 1.35; padding-right: 26px; }

  .brand {
    position: absolute;
    display: flex;
    align-items: center;
    gap: 10px;
    color: var(--navy);
    font-size: 30px;
    letter-spacing: 1px;
    white-space: nowrap;
  }
  .brand-mark {
    width: 30px; height: 30px;
    border-radius: 50%;
    border: 3px solid var(--orange);
    box-sizing: border-box;
  }
  .card-front .brand { left: 34px; bottom: 36px; }
  .card-back .brand { left: 34px; top: 28px; font-size: 27px; }
  .card-back .brand-mark { width: 28px; height: 28px; }
</style>
</head>
<body>
<main class="canvas">

  <section class="card card-front" aria-label="Business card front">
    <div class="front-top"></div>
    <div class="front-rule"></div>

    <div class="contact">
      <div class="contact-name">Dana Whitfield, SPHR</div>
      <div class="contact-title">Managing Director</div>
      <div class="contact-lines">
        <span>303-555-0148</span>
        <svg viewBox="0 0 16 16" aria-hidden="true"><path d="M4 1.5 6.2 4.3 4.9 6a8 8 0 0 0 5 5l1.7-1.3 2.8 2.2-1.4 2.3C7.6 14 2 8.4 1.8 3Z" fill="currentColor"/></svg>
        <span>dana@talentsummit.com</span>
        <svg viewBox="0 0 16 16" aria-hidden="true"><rect x="1.5" y="3.5" width="13" height="9" fill="currentColor"/><path d="M1.5 3.5 8 9l6.5-5.5" stroke="var(--navy)" stroke-width="1.3" fill="none"/></svg>
        <span>www.talentsummit.com</span>
        <svg viewBox="0 0 16 16" aria-hidden="true"><circle cx="8" cy="8" r="6.5" fill="none" stroke="currentColor" stroke-width="1.4"/><ellipse cx="8" cy="8" rx="2.8" ry="6.5" fill="none" stroke="currentColor" stroke-width="1.2"/><path d="M1.5 8h13" stroke="currentColor" stroke-width="1.2"/></svg>
      </div>
      <div class="contact-address">Here your company or<br>home address</div>
    </div>

    <div class="brand"><span class="brand-mark"></span><span class="brand-name">TALENT SUMMIT</span></div>
  </section>

  <section class="card card-back" aria-label="Business card back, to-do note lines">
    <div class="brand"><span class="brand-mark"></span><span class="brand-name">TALENT SUMMIT</span></div>
    <svg class="card-art" viewBox="0 0 540 308" preserveAspectRatio="none" aria-hidden="true">
      <g stroke="var(--navy-line)" stroke-width="1.6">
        <line x1="34" y1="110" x2="506" y2="110"/>
        <line x1="34" y1="158" x2="506" y2="158"/>
        <line x1="34" y1="206" x2="506" y2="206"/>
        <line x1="34" y1="254" x2="506" y2="254"/>
      </g>
    </svg>
  </section>

</main>
</body>
</html>
```